527 Process Infographic Redesign

We need a redesign of our companies reconstruction process chart that is posted in our construction offices. We would like the design to use flowchart or decision tree in functional approach. This will be used in large format poster as well as on pdfs so will need to be bold yet clear in communication.

Industry/Entity Type

Construction

Font styles to use
Sans Serif

Colors
EE7325
F08F49
F5BC92
FAE3D3
FDF4ED

Requirements
Must have
• same info presented in current design

```html
<!DOCTYPE html>
<html lang="en">
<head>
<meta charset="utf-8">
<title>527 Construction — Our Process</title>
<link rel="stylesheet" href="https://fonts.googleapis.com/css2?family=Montserrat:wght@400;600;700;800;900&family=Oswald:wght@500;600&display=swap">
<style>
:root{
  --page:#eeeeee;
  --paper:#ffffff;
  --ink:#0e3a4a;
  --brand:#d2601a;
  --band-1:#d86a2c;
  --band-2:#ee8e48;
  --band-3:#efa66b;
  --band-4:#ecb07e;
  --head-1:#f3a878;
  --head-2:#d6621e;
  --head-3:#e2843f;
  --head-4:#f6cba8;
  --recon:#e2dea6;
  --gm:#f7c23a;
  --pm:#f26b5b;
  --estimator:#3fbfef;
  --accounting:#4caf2a;
  --inactive:#bdbdbd;
  --line:#ffffff;
}
html,body{margin:0;width:1200px;height:1200px;overflow:hidden;background:var(--page)}
.poster{position:absolute;left:0;top:140px;width:1200px;height:921px;display:block}
.sheet{fill:var(--paper)}
.band-intimation{fill:var(--band-1)}
.band-planning{fill:var(--band-2)}
.band-execution{fill:var(--band-3)}
.band-closeout{fill:var(--band-4)}
.phase{font-family:Montserrat,sans-serif;font-weight:900;font-size:74px;letter-spacing:-3px}
.phase-1{fill:var(--head-1)}.phase-2{fill:var(--head-2)}.phase-3{fill:var(--head-3)}.phase-4{fill:var(--head-4)}
.brand-name{font-family:Montserrat,sans-serif;font-weight:900;fill:var(--brand)}
.title{font-family:Montserrat,sans-serif;font-weight:900;font-size:100px;fill:var(--brand);letter-spacing:-2px}
.subtitle{font-family:Montserrat,sans-serif;font-weight:400;font-size:26px;fill:#222;letter-spacing:-0.5px}
.legend text{font-family:Montserrat,sans-serif;font-size:18px;fill:var(--ink)}
.legend circle{fill:#fff;stroke-width:4}
.node rect{fill:#fff;stroke-width:4}
.node text,.t{font-family:Montserrat,sans-serif;font-size:15px;fill:var(--ink)}
.node .sm{font-size:11px}
.b{font-weight:700}
.muted{fill:#9a9a9a}
.c{text-anchor:middle}
.recon rect,.recon circle{stroke:var(--recon)}
.gm rect,.gm circle{stroke:var(--gm)}
.pm rect,.pm circle{stroke:var(--pm)}
.estimator rect,.estimator circle{stroke:var(--estimator)}
.accounting rect,.accounting circle{stroke:var(--accounting)}
.inactive rect,.inactive circle{stroke:var(--inactive)}
.plain rect{stroke:none}
.decision circle{fill:#fff;stroke-width:5}
.decision text{font-family:Oswald,sans-serif;font-weight:600;fill:var(--ink);text-anchor:middle}
.decision.open circle{stroke:none}
.decision.green circle{stroke:var(--accounting)}
.label{font-family:Oswald,sans-serif;font-weight:500;font-size:19px;fill:#fff;text-anchor:middle}
.flow path{fill:none;stroke:var(--line);stroke-width:1.6;stroke-dasharray:6 5;opacity:.85}
</style>
</head>
<body>
<svg class="poster" viewBox="87 290 1758 1350" xmlns="http://www.w3.org/2000/svg">
  <defs>
    <marker id="arrow" viewBox="0 0 10 10" refX="8" refY="5" markerWidth="6" markerHeight="6" orient="auto">
      <path d="M1 1 L8 5 L1 9" fill="none" stroke="#fff" stroke-width="1.6"/>
    </marker>
  </defs>

  <rect class="sheet" x="87" y="290" width="1758" height="1350"/>

  <!-- header -->
  <g class="brand">
    <rect x="140" y="352" width="30" height="30" fill="var(--brand)"/>
    <text class="brand-name" x="182" y="382" font-size="38">527</text>
    <text class="brand-name" x="140" y="440" font-size="29">CONSTRUCTION</text>
  </g>
  <text class="title" x="966" y="425" text-anchor="middle">OUR PROCESS</text>
  <text class="subtitle" x="966" y="475" text-anchor="middle">Job Notes are to be created at each step in this process.</text>

  <g class="legend">
    <g class="recon"><circle cx="1425" cy="362" r="11"/><text x="1449" y="368">Recon Coordinator</text></g>
    <g class="gm"><circle cx="1425" cy="410" r="11"/><text x="1449" y="417">GM/Owner</text></g>
    <g class="pm"><circle cx="1425" cy="457" r="11"/><text x="1449" y="463">Project Manager</text></g>
    <g class="estimator"><circle cx="1656" cy="361" r="11"/><text x="1680" y="367">Estimator</text></g>
    <g class="accounting"><circle cx="1656" cy="409" r="11"/><text x="1680" y="415">Accounting</text></g>
    <g class="inactive"><circle cx="1656" cy="457" r="11"/><text x="1680" y="463">Inactive step</text></g>
  </g>

  <!-- phase bands -->
  <rect class="band-intimation" x="110" y="528" width="424" height="1090"/>
  <rect class="band-planning" x="533" y="528" width="433" height="1090"/>
  <rect class="band-execution" x="965" y="528" width="438" height="1090"/>
  <rect class="band-closeout" x="1402" y="528" width="421" height="1090"/>
  <text class="phase phase-1" x="106" y="600">Intimation</text>
  <text class="phase phase-2" x="527" y="600">Planning</text>
  <text class="phase phase-3" x="962" y="600">Execution</text>
  <text class="phase phase-4" x="1398" y="600">Closeout</text>

  <!-- connectors -->
  <g class="flow">
    <path d="M223 700 V716" marker-end="url(#arrow)"/>
    <path d="M223 813 V836" marker-end="url(#arrow)"/>
    <path d="M311 873 H366" marker-end="url(#arrow)"/>
    <path d="M433 920 V950 H223 V960"/>
    <path d="M399 950 V960"/>
    <path d="M406 1111 V1128" marker-end="url(#arrow)"/>
    <path d="M223 1224 V1248" marker-end="url(#arrow)"/>
    <path d="M400 1224 V1248" marker-end="url(#arrow)"/>
    <path d="M223 1317 V1354" marker-end="url(#arrow)"/>
    <path d="M223 1421 V1460 H308" marker-end="url(#arrow)"/>
    <path d="M262 1490 H235 V1518" marker-end="url(#arrow)"/>
    <path d="M510 1493 H552 V668 H576" marker-end="url(#arrow)"/>
    <path d="M660 727 V750" marker-end="url(#arrow)"/>
    <path d="M726 786 H755" marker-end="url(#arrow)"/>
    <path d="M757 857 H638 V881" marker-end="url(#arrow)"/>
    <path d="M638 939 V958" marker-end="url(#arrow)"/>
    <path d="M726 990 H836 V1007" marker-end="url(#arrow)"/>
    <path d="M752 1114 H638 V1132" marker-end="url(#arrow)"/>
    <path d="M738 1174 H766" marker-end="url(#arrow)"/>
    <path d="M836 1202 V1230" marker-end="url(#arrow)"/>
    <path d="M646 1285 H618 V1366" marker-end="url(#arrow)"/>
    <path d="M738 1402 H770" marker-end="url(#arrow)"/>
    <path d="M772 1452 H638 V1480" marker-end="url(#arrow)"/>
    <path d="M800 1518 H995 V668 H1016" marker-end="url(#arrow)"/>
    <path d="M1165 670 H1278 V690" marker-end="url(#arrow)"/>
    <path d="M1205 784 H1162" marker-end="url(#arrow)"/>
    <path d="M1160 818 V852 H1212" marker-end="url(#arrow)"/>
    <path d="M1112 830 V876" marker-end="url(#arrow)"/>
    <path d="M1280 893 V913" marker-end="url(#arrow)"/>
    <path d="M1272 973 V998" marker-end="url(#arrow)"/>
    <path d="M1194 1045 H1184" marker-end="url(#arrow)"/>
    <path d="M1095 1082 V1106" marker-end="url(#arrow)"/>
    <path d="M1262 1165 H1290" marker-end="url(#arrow)"/>
    <path d="M1309 1206 V1240" marker-end="url(#arrow)"/>
    <path d="M1385 1180 H1392 V1444" marker-end="url(#arrow)"/>
    <path d="M1284 1462 H1190" marker-end="url(#arrow)"/>
    <path d="M1106 1485 V1502" marker-end="url(#arrow)"/>
    <path d="M1188 1553 H1214" marker-end="url(#arrow)"/>
    <path d="M1374 1570 H1428 V682 H1628 V690" marker-end="url(#arrow)"/>
    <path d="M1711 758 V826 H1676" marker-end="url(#arrow)"/>
    <path d="M1581 858 H1544 V896" marker-end="url(#arrow)"/>
    <path d="M1673 858 H1719 V896" marker-end="url(#arrow)"/>
    <path d="M1722 985 V1017" marker-end="url(#arrow)"/>
    <path d="M1640 1028 H1617" marker-end="url(#arrow)"/>
    <path d="M1686 1088 V1116 H1614" marker-end="url(#arrow)"/>
    <path d="M1543 1160 V1212" marker-end="url(#arrow)"/>
    <path d="M1612 1150 H1615 V1188 H1664" marker-end="url(#arrow)"/>
    <path d="M1536 1272 V1290" marker-end="url(#arrow)"/>
    <path d="M1733 1254 V1290" marker-end="url(#arrow)"/>
    <path d="M1536 1375 V1398" marker-end="url(#arrow)"/>
    <path d="M1733 1375 V1410" marker-end="url(#arrow)"/>
    <path d="M1560 1553 H1654" marker-end="url(#arrow)"/>
  </g>

  <!-- intimation -->
  <g class="node gm"><rect x="143" y="637" width="138" height="62" rx="8"/><text x="165" y="676" font-size="20" style="font-size:20px;font-weight:600">New Lead</text></g>
  <g class="node recon"><rect x="143" y="720" width="310" height="93" rx="8"/>
    <text x="162" y="752">Enter into JobBase Create FileBox</text><text x="162" y="774">Folder Setup SiteCam Date</text><text x="162" y="796">Received</text></g>
  <g class="node pm"><rect x="143" y="840" width="168" height="65" rx="8"/><text x="162" y="866">Contact Lead</text><text x="162" y="888">Lead Contacted</text></g>
  <g class="decision green"><circle cx="420" cy="871" r="47"/><text x="420" y="881" font-size="23">RESTORA</text></g>
  <text class="label" x="223" y="979">YES</text><text class="label" x="399" y="979">NO</text>
  <g class="node pm"><rect x="145" y="991" width="152" height="86" rx="8"/><text class="c" x="219" y="1018">Coordinate with</text><text class="c" x="219" y="1038">Mitigation</text><text class="c" x="219" y="1058">Manager</text></g>
  <g class="node pm"><rect x="319" y="991" width="164" height="120" rx="8"/>
    <text class="c b" x="401" y="1018">Site Inspection</text><text class="c" x="401" y="1038">Scope Sheets,</text><text class="c" x="401" y="1058">PlanSketch &amp;</text><text class="c" x="401" y="1077">Interim Agreement</text><text class="c" x="401" y="1097">Site Inspected</text></g>
  <g class="node estimator"><rect x="143" y="1132" width="340" height="92" rx="8"/>
    <text class="b" x="162" y="1163">Estimate Creation</text><text x="162" y="1183">Estimate Requested | Estimate Started |</text><text x="162" y="1203">Estimated Completed | Estimate On Hold</text></g>
  <g class="node pm"><rect x="145" y="1253" width="152" height="64" rx="8"/><text class="c" x="219" y="1281">Estimate</text><text class="c" x="219" y="1301">Review</text></g>
  <g class="node gm"><rect x="329" y="1253" width="155" height="84" rx="8"/><text class="c b" x="406" y="1281">Estimate</text><text class="c b" x="406" y="1301">Approval by</text><text class="c b" x="406" y="1320">GM if &gt; $75K</text></g>
  <g class="node pm"><rect x="143" y="1358" width="340" height="63" rx="8"/><text class="b" x="162" y="1388">Submit Estimate Customer &amp; Adjuster |</text><text class="muted" x="162" y="1408">Estimate Submitted</text></g>
  <g class="decision green"><circle cx="366" cy="1493" r="55"/><text x="366" y="1490" font-size="24">ESTIMATE</text><text x="366" y="1514" font-size="24">APPROVED</text></g>
  <text class="label" x="278" y="1496">NO</text><text class="label" x="489" y="1498">YES</text>
  <g class="node recon"><rect x="128" y="1523" width="162" height="63" rx="8"/><text class="c b" x="210" y="1550">Email Notification</text><text class="c" x="210" y="1570">Job Not Sold</text></g>

  <!-- planning -->
  <g class="node estimator"><rect x="579" y="634" width="309" height="93" rx="8"/>
    <text class="b" x="598" y="665">Print Reports</text><text x="598" y="687">Scope, Components,Summary w/</text><text x="598" y="709">Detail, Approved Estimate</text></g>
  <g class="node recon"><rect x="580" y="753" width="146" height="58" rx="8"/><text x="597" y="778">Create &amp;</text><text x="597" y="798">Share Budget</text></g>
  <g class="node pm"><rect x="759" y="755" width="158" height="117" rx="8"/>
    <text class="c" x="838" y="782">Build Budget</text>
    <text class="c" x="838" y="802">Develop <tspan class="b">Payment</tspan></text>
    <text class="c" x="838" y="822"><tspan class="b">Schedule</tspan> Create</text>
    <text class="c b" x="838" y="841">Material Selection</text>
    <text class="c b" x="838" y="861">Sheet</text></g>
  <g class="node pm"><rect x="582" y="885" width="298" height="54" rx="8"/><text x="597" y="917">Walk job with Subs and call vendors</text></g>
  <g class="node gm"><rect x="580" y="962" width="146" height="58" rx="8"/><text x="597" y="997">Budget Review</text></g>
  <g class="node inactive"><rect x="754" y="1011" width="163" height="118" rx="8"/>
    <text class="c" x="835" y="1038">Create</text><text class="c b" x="835" y="1058">Work Schedule</text><text class="c" x="835" y="1078">Target Start Date</text><text class="c" x="835" y="1097">Target Completion</text><text class="c" x="835" y="1117">Date</text></g>
  <g class="node accounting"><rect x="594" y="1136" width="144" height="56" rx="6"/><text x="610" y="1160">Invoice</text><text x="610" y="1180">Deductible</text></g>
  <g class="node accounting"><rect x="770" y="1146" width="145" height="56" rx="6"/><text x="786" y="1180">Invoice Deposit</text></g>
  <g class="node plain"><rect x="648" y="1235" width="268" height="112" rx="6"/>
    <text class="b" x="668" y="1259">Create Customer Packet</text><text x="668" y="1279">with Work Authorization,</text><text x="668" y="1299">Payment Schedule, Mortgage</text><text x="668" y="1318">Authorization, Invoices and</text><text x="668" y="1338">Material Selection Sheet</text></g>
  <g class="node gm"><rect x="594" y="1370" width="144" height="56" rx="6"/><text x="610" y="1396">Management</text><text x="610" y="1416">Review</text></g>
  <g class="node pm"><rect x="774" y="1370" width="144" height="102" rx="8"/>
    <text class="c b" x="846" y="1398">Customer</text><text class="c b" x="846" y="1418">Onboarding</text><text class="c b" x="846" y="1438">Meeting</text><text class="c" x="846" y="1458">Work Auth &amp; PS</text></g>
  <g class="node pm"><rect x="582" y="1485" width="218" height="68" rx="8"/><text x="597" y="1516">Provide Customer Copies</text><text x="597" y="1536">of Onboarding Docs</text></g>

  <!-- execution -->
  <g class="node inactive"><rect x="1020" y="640" width="145" height="58" rx="8"/><text x="1032" y="663">Create</text><text x="1032" y="683">Purchase Orders</text></g>
  <g class="node recon"><rect x="1207" y="694" width="141" height="104" rx="8"/>
    <text class="c" x="1278" y="720">Submit WA to</text><text class="c" x="1278" y="740">Adjuster</text><text class="c" x="1278" y="760">Requesting</text><text class="c b" x="1278" y="779">Depreciation</text></g>
  <g class="decision open"><circle cx="1112" cy="783" r="47"/><text x="1112" y="792" font-size="23">&gt;$25,000</text></g>
  <text class="label" x="1091" y="863">YES</text><text class="label" x="1188" y="858">NO</text>
  <g class="node recon"><rect x="1216" y="829" width="133" height="64" rx="8"/><text class="c" x="1282" y="855">Pull Permit</text><text class="c" x="1282" y="875">if required</text></g>
  <g class="node recon"><rect x="1020" y="880" width="132" height="92" rx="8"/><text class="c" x="1086" y="913">File Signed</text><text class="c" x="1086" y="933">Contract with</text><text class="c" x="1086" y="952">Courthouse</text></g>
  <g class="node pm"><rect x="1186" y="917" width="164" height="56" rx="8"/><text x="1201" y="952">Initiation Checklist</text></g>
  <g class="node pm"><rect x="1016" y="1002" width="164" height="80" rx="8"/><text x="1031" y="1029">On Site Meetings</text><text x="1031" y="1049">with Customer,</text><text x="1031" y="1068">PM &amp; Subs</text></g>
  <g class="node pm"><rect x="1196" y="1002" width="164" height="80" rx="8"/><text x="1211" y="1029">Secure Signed</text><text x="1211" y="1049">Scopes from Subs</text><text x="1211" y="1068">&amp; Vendors</text></g>
  <g class="node pm"><rect x="1016" y="1110" width="246" height="100" rx="8"/>
    <text class="b" x="1031" y="1138">In Progress</text><text x="1031" y="1158">Regular Communication,</text><text x="1031" y="1178">Job Notes, Photos, Site Visits,</text><text x="1031" y="1198">Change Orders <tspan class="b">Work Start</tspan></text></g>
  <g class="decision open"><circle cx="1339" cy="1160" r="46"/><text x="1339" y="1160" font-size="18">ADDITIONAL</text><text x="1339" y="1181" font-size="18">SCOPE</text></g>

  <g class="node pm"><rect x="1016" y="1224" width="78" height="57" rx="5"/><text class="sm" x="1024" y="1244">Draw 2</text><text class="sm" x="1024" y="1257">Inspections</text><text class="sm" x="1024" y="1270">/ COS</text></g>
  <g class="node pm"><rect x="1099" y="1224" width="78" height="57" rx="5"/><text class="sm" x="1107" y="1244">Draw 2</text><text class="sm" x="1107" y="1257">Inspections</text><text class="sm" x="1107" y="1270">/ COS</text></g>
  <g class="node pm"><rect x="1180" y="1224" width="78" height="57" rx="5"/><text class="sm" x="1188" y="1244">Draw 2</text><text class="sm" x="1188" y="1257">Inspections</text><text class="sm" x="1188" y="1270">/ COS</text></g>
  <g class="node accounting"><rect x="1016" y="1290" width="78" height="46" rx="5"/><text class="sm" x="1024" y="1311">Invoice</text><text class="sm" x="1024" y="1324">from PS</text></g>
  <g class="node accounting"><rect x="1099" y="1290" width="78" height="46" rx="5"/><text class="sm" x="1107" y="1311">Invoice</text><text class="sm" x="1107" y="1324">from PS</text></g>
  <g class="node accounting"><rect x="1180" y="1290" width="78" height="46" rx="5"/><text class="sm" x="1188" y="1311">Invoice</text><text class="sm" x="1188" y="1324">from PS</text></g>
  <g class="node pm"><rect x="1016" y="1346" width="78" height="46" rx="5"/><text class="sm" x="1024" y="1366">Verify Docs</text><text class="sm" x="1024" y="1379">&amp; COS Call</text></g>
  <g class="node pm"><rect x="1099" y="1346" width="78" height="46" rx="5"/><text class="sm" x="1107" y="1366">Verify Docs</text><text class="sm" x="1107" y="1379">&amp; COS Call</text></g>
  <g class="node pm"><rect x="1180" y="1346" width="78" height="46" rx="5"/><text class="sm" x="1188" y="1366">Verify Docs</text><text class="sm" x="1188" y="1379">&amp; COS Call</text></g>

  <text class="label" x="1309" y="1228">YES</text><text class="label" x="1390" y="1308">NO</text>
  <g class="node pm"><rect x="1280" y="1243" width="84" height="58" rx="5"/><text class="sm" x="1287" y="1263">Change</text><text class="sm" x="1287" y="1276">Order/</text><text class="sm" x="1287" y="1289">Supplement</text></g>
  <g class="node pm"><rect x="1280" y="1310" width="84" height="46" rx="5"/><text class="sm" x="1287" y="1337">Document</text></g>
  <g class="node accounting"><rect x="1280" y="1365" width="84" height="46" rx="5"/><text class="sm" x="1287" y="1392">Invoice</text></g>
  <g class="decision open"><circle cx="1332" cy="1470" r="46"/><text x="1332" y="1471" font-size="16">SIGNIFICANTLY</text><text x="1332" y="1490" font-size="16">COMPLETE</text></g>
  <text class="label" x="1234" y="1468">YES</text>
  <g class="node pm"><rect x="1024" y="1427" width="162" height="58" rx="8"/><text x="1043" y="1462">Signed Punchlist</text></g>
  <g class="node pm"><rect x="1024" y="1506" width="164" height="80" rx="8"/><text x="1043" y="1532">Certificate of</text><text x="1043" y="1552">Completion</text><text x="1043" y="1572">Work Complete</text></g>
  <g class="node pm"><rect x="1218" y="1537" width="156" height="62" rx="8"/><text x="1233" y="1565">Submit to</text><text x="1233" y="1585">Insurance Carrier</text></g>

  <!-- closeout -->
  <g class="node pm"><rect x="1455" y="694" width="152" height="64" rx="8"/><text class="c" x="1530" y="721">Request</text><text class="c" x="1530" y="741">Searchly Review</text></g>
  <g class="node pm"><rect x="1633" y="694" width="152" height="64" rx="8"/><text class="c" x="1711" y="721">Final Review:</text><text class="c" x="1711" y="741">Supplement</text></g>
  <g class="decision open"><circle cx="1627" cy="828" r="46"/><text x="1627" y="835" font-size="18">SUPPLEMENT</text></g>
  <text class="label" x="1541" y="889">YES</text><text class="label" x="1717" y="889">NO</text>
  <g class="node estimator"><rect x="1461" y="901" width="152" height="62" rx="8"/><text class="c" x="1537" y="928">Write Final</text><text class="c" x="1537" y="948">Supplement</text></g>
  <g class="node pm"><rect x="1642" y="901" width="154" height="84" rx="8"/><text class="c" x="1719" y="928">Submit</text><text class="c" x="1719" y="948">Final Invoice to</text><text class="c" x="1719" y="968">Customer &amp; Client</text></g>
  <g class="node recon"><rect x="1461" y="985" width="152" height="64" rx="8"/><text class="c" x="1537" y="1012">Submit to</text><text class="c" x="1537" y="1032">Insurance Agent</text></g>
  <g class="node recon"><rect x="1642" y="1021" width="154" height="64" rx="8"/><text class="c" x="1717" y="1048">Certificate of</text><text class="c" x="1717" y="1068">Satisfaction</text></g>
  <g class="decision open"><circle cx="1565" cy="1113" r="46"/><text x="1565" y="1112" font-size="22">BALANCE</text><text x="1565" y="1133" font-size="20">PAID</text><text x="1565" y="1146" font-size="9">PAID IN FULL</text></g>
  <text class="label" x="1543" y="1194">YES</text><text class="label" x="1639" y="1189">NO</text>
  <g class="node pm"><rect x="1668" y="1160" width="132" height="94" rx="8"/><text class="c" x="1734" y="1184">Stay in Contact</text><text class="c" x="1734" y="1204">with Customer</text><text class="c" x="1734" y="1223">Awaiting</text><text class="c" x="1734" y="1243">Payment</text></g>
  <g class="node plain"><rect x="1465" y="1216" width="146" height="56" rx="6"/><text class="c b" x="1538" y="1240">Verify Job File</text><text class="c b" x="1538" y="1260">is Complete</text></g>
  <text class="label" x="1733" y="1284">30 DAYS</text>
  <g class="node accounting"><rect x="1448" y="1295" width="200" height="80" rx="8"/><text x="1459" y="1320">Pay remaining expenses</text><text x="1459" y="1340">/recognize remaining</text><text x="1459" y="1360">income.</text></g>
  <g class="node recon"><rect x="1668" y="1295" width="132" height="80" rx="8"/><text x="1681" y="1322">Certified Letter</text><text x="1681" y="1342">Demand of</text><text x="1681" y="1362">Payment</text></g>
  <text class="label" x="1733" y="1403">60 DAYS</text>
  <g class="node recon"><rect x="1448" y="1402" width="152" height="100" rx="8"/><text x="1459" y="1428">Submit any</text><text x="1459" y="1448">commission/</text><text x="1459" y="1468">bonus information</text><text x="1459" y="1488">to accounting.</text></g>
  <g class="node recon"><rect x="1668" y="1415" width="132" height="64" rx="8"/><text x="1681" y="1443">Turn over to</text><text x="1681" y="1463">Collections</text></g>
  <g class="node accounting"><rect x="1448" y="1523" width="112" height="56" rx="6"/><text x="1460" y="1557">File Closed</text></g>
  <g class="node plain"><rect x="1658" y="1520" width="138" height="72" rx="6"/><text class="b" x="1665" y="1542">File Review</text><text x="1665" y="1562">Gross Margin,</text><text x="1665" y="1582">COS, Cycle Time</text></g>
</svg>
</body>
</html>
```